Music Industry Business Needs a Business Card Design

Copper Lantern is an audio mastering company that has been in business for 20 years. Mastering is the final creative step in the music production chain. Our job is to make the music sound as good as it possibly can prior to release to the public. Our world is technical, artistic, precise. We work on everything from independent artists to the music for the Grandfield Cup. We are looking for a new, more modern business card design. I am uploading a copy of our logo, although it doesn't absolutely need to be included in the design.

Target Market(s)

Music Industry Professionals

Industry/Entity Type

Business

Contact Information for Business Card

Address, Phone, Email, Website, Name, Job Title

Font styles to use
Sans Serif

Requirements
Must have
• Sorry, but I don't have any concrete things to request. If I had a clear idea of what I want, I would probably just design something myself. I am looking for fresh input and thought I would try this.
Should not have
• Anything that is typical, such as headphones or the like.

```html
<!DOCTYPE html>
<html lang="en">
<head>
<meta charset="utf-8">
<title>Copper Lantern – Business Card</title>
<link rel="stylesheet" href="https://fonts.googleapis.com/css2?family=Mulish:wght@400;700&display=swap">
<style>
  :root {
    --stage: #2a2c2f;
    --card-black: #0c0d0f;
    --card-black-soft: #1d1f23;
    --panel-light: #f5f9ff;
    --panel-blue: #3f8ff0;
    --stripe-blue: #3b8de6;
    --stripe-white: #ffffff;
    --text-white: #ffffff;
    --web-cyan: #4fd6ea;
    --logo-cyan: #2fb4cc;
  }
  html, body {
    margin: 0;
    width: 1200px;
    height: 1000px;
    overflow: hidden;
    background: var(--stage);
    font-family: "Mulish", sans-serif;
  }
  .card {
    position: absolute;
    left: 100px;
    top: 214px;
    width: 1000px;
    height: 572px;
    border-radius: 6px;
    overflow: hidden;
    box-shadow: 0 20px 50px rgba(0,0,0,0.5);
  }
  .card-art {
    position: absolute;
    inset: 0;
    width: 1000px;
    height: 572px;
  }
  .brand {
    position: absolute;
    left: 560px;
    top: 34px;
    display: flex;
    align-items: center;
    gap: 12px;
    color: var(--logo-cyan);
    font-size: 22px;
    font-weight: 400;
    letter-spacing: 2px;
    text-transform: uppercase;
  }
  .brand-dot {
    width: 14px;
    height: 14px;
    border-radius: 50%;
    background: var(--logo-cyan);
  }
  .contact {
    position: absolute;
    right: 110px;
    top: 196px;
    text-align: right;
    color: var(--text-white);
    line-height: 1.2;
  }
  .contact-name {
    font-size: 42px;
    font-weight: 700;
    margin: 0;
  }
  .contact-role {
    font-size: 28px;
    margin: 2px 0 14px;
  }
  .contact-line {
    font-size: 30px;
    margin: 0 0 4px;
  }
  .website {
    position: absolute;
    right: 130px;
    bottom: 34px;
    color: var(--web-cyan);
    font-size: 40px;
    letter-spacing: 0.5px;
  }
</style>
</head>
<body>
  <section class="card" aria-label="Copper Lantern business card">
    <svg class="card-art" viewBox="0 0 1000 572" aria-hidden="true">
      <defs>
        <linearGradient id="card-bg" x1="0" y1="0" x2="1" y2="1">
          <stop offset="0" stop-color="var(--card-black-soft)"/>
          <stop offset="1" stop-color="var(--card-black)"/>
        </linearGradient>
        <linearGradient id="panel-fill" x1="0" y1="0" x2="1" y2="1">
          <stop offset="0" stop-color="var(--panel-light)"/>
          <stop offset="0.45" stop-color="#a9cdf8"/>
          <stop offset="1" stop-color="var(--panel-blue)"/>
        </linearGradient>
      </defs>
      <rect class="card-base" width="1000" height="572" fill="url(#card-bg)"/>
      <path class="panel" d="M70,40 C380,30 620,110 920,175 L920,480 C700,470 350,330 70,345 Z" fill="url(#panel-fill)"/>
      <path class="edge-top-blue" d="M70,30 C380,20 620,100 920,165" fill="none" stroke="var(--stripe-blue)" stroke-width="6"/>
      <path class="edge-bottom-white" d="M70,360 C350,345 700,485 920,495" fill="none" stroke="var(--stripe-white)" stroke-width="6"/>
      <path class="edge-bottom-blue" d="M70,374 C350,359 700,499 920,509" fill="none" stroke="var(--stripe-blue)" stroke-width="5"/>
      <line class="rule-left-white" x1="48" y1="0" x2="48" y2="572" stroke="var(--stripe-white)" stroke-width="5"/>
      <line class="rule-left-blue" x1="58" y1="0" x2="58" y2="572" stroke="var(--stripe-blue)" stroke-width="4"/>
      <line class="rule-right-blue" x1="938" y1="0" x2="938" y2="572" stroke="var(--stripe-blue)" stroke-width="4"/>
      <line class="rule-right-white" x1="950" y1="0" x2="950" y2="572" stroke="var(--stripe-white)" stroke-width="5"/>
    </svg>

    <div class="brand"><span class="brand-dot"></span>Copper Lantern</div>

    <div class="contact">
      <p class="contact-name">Mark Ellison</p>
      <p class="contact-role">manager</p>
      <p class="contact-line">555 418 2760</p>
      <p class="contact-line">14 Harbor Lane</p>
      <p class="contact-line">info@copperlantern.com</p>
    </div>

    <div class="website">www.copperlantern.com</div>
  </section>
</body>
</html>
```